Business Card Design for general contractor or developer

General Contractors. We build new buildings as well as redesign and/or remodel existing buildings. Mostly residential, but we want to expand to commercial as well, so we want the design not to be residential specific.We want the design to be modern, but necessarily minimalistic. A monogram type is also a consideration, but would like to see all ideas.

Target Market(s)

Real estate investors, homeowners, future homeowners, commercial building owners

Industry/Entity Type

Contractor

Contact Information for Business Card

BRIMCOVE Developers Corp, 6127 NE 318th Avenue Suite 241 Miami Lakes, FL 33482, Curtis Ortega, (305) 472-1803, curtis@quarvinta.com

Font styles to use
Other font styles liked:
• Modern type font

Requirements
Must have
• Must be modern looking
Nice to have
• Metallic type or a standout feature
Should not have
• Tools, floorplans

```html
<!DOCTYPE html>
<html lang="en">
<head>
<meta charset="utf-8">
<title>BRIMCOVE Developers Corp — Business Card</title>
<link href="https://fonts.googleapis.com/css2?family=Open+Sans:wght@400;600;700&display=swap" rel="stylesheet">
<style>
  :root {
    --page: #e6e3e0;
    --card: #161616;
    --card-edge: #0c0c0c;
    --silver: #b9b9b9;
    --silver-dark: #8a8a8a;
    --white: #f4f4f4;
    --name-grey: #9a9a9a;
    --rule: #3a3a3a;
  }
  * { box-sizing: border-box; margin: 0; padding: 0; }
  html, body { width: 1200px; height: 787px; overflow: hidden; }
  body {
    background: var(--page);
    font-family: "Open Sans", Arial, sans-serif;
    display: flex;
    align-items: center;
    justify-content: center;
    gap: 40px;
  }
  .card {
    width: 520px;
    height: 297px;
    background: var(--card);
    border: 1px solid var(--card-edge);
    border-radius: 4px;
    position: relative;
    overflow: hidden;
  }
  /* Front */
  .card--front {
    display: flex;
    flex-direction: column;
    align-items: center;
    justify-content: center;
    gap: 18px;
  }
  .brand-mark {
    width: 58px;
    height: 58px;
    border-radius: 50%;
    background: var(--silver-dark);
  }
  .brand-name {
    font-weight: 400;
    font-size: 26px;
    letter-spacing: 0.3px;
    color: var(--silver);
  }
  /* Back */
  .card--back {
    display: flex;
    align-items: center;
    padding: 0 28px 0 30px;
  }
  .back-brand {
    flex: 0 0 250px;
    display: flex;
    flex-direction: column;
    align-items: center;
    gap: 14px;
  }
  .back-brand .brand-mark { width: 48px; height: 48px; background: var(--white); }
  .back-brand .brand-name { font-size: 19px; color: var(--white); }
  .divider {
    width: 1px;
    height: 150px;
    background: linear-gradient(to bottom, transparent, var(--rule), transparent);
    margin: 0 18px 0 6px;
  }
  .contact { color: var(--white); }
  .contact__name {
    font-weight: 700;
    font-size: 21px;
    color: var(--name-grey);
    line-height: 1.1;
  }
  .contact__title { font-size: 12px; color: var(--silver); margin-bottom: 8px; }
  .contact__address { font-size: 12px; line-height: 1.45; margin-bottom: 6px; }
  .contact__list { list-style: none; font-size: 12px; line-height: 1.65; }
  .contact__list li { display: flex; align-items: center; gap: 7px; }
  .icon { width: 10px; height: 10px; fill: var(--silver-dark); flex: none; }
</style>
</head>
<body>
  <section class="card card--front" aria-label="Card front">
    <span class="brand-mark" aria-hidden="true"></span>
    <span class="brand-name">BRIMCOVE Developers Corp</span>
  </section>

  <section class="card card--back" aria-label="Card back">
    <div class="back-brand">
      <span class="brand-mark" aria-hidden="true"></span>
      <span class="brand-name">BRIMCOVE Developers Corp</span>
    </div>
    <div class="divider"></div>
    <div class="contact">
      <p class="contact__name">Dorian Hale</p>
      <p class="contact__title">Managing Member</p>
      <p class="contact__address">2290 Meridian Loop,<br>Larkfield, CA 95403</p>
      <ul class="contact__list">
        <li><svg class="icon" viewBox="0 0 10 10"><path d="M2 0h2l1 2.5-1.3 1a5 5 0 0 0 2.8 2.8l1-1.3L10 6v2a2 2 0 0 1-2 2A8 8 0 0 1 0 2a2 2 0 0 1 2-2z"/></svg>(707) 484-2210</li>
        <li><svg class="icon" viewBox="0 0 10 10"><path d="M2 0h5v3H2zM0 4h10v6H0zm2 2v1h6V6z"/></svg>(707) 484-2211</li>
        <li><svg class="icon" viewBox="0 0 10 10"><path d="M2.5 0h5a1 1 0 0 1 1 1v8a1 1 0 0 1-1 1h-5a1 1 0 0 1-1-1V1a1 1 0 0 1 1-1zM3 1.5v6h4v-6z"/></svg>(707) 319-5528</li>
        <li><svg class="icon" viewBox="0 0 10 10"><path d="M0 1.5h10v7H0zM1 2.5 5 5.5l4-3z" fill-rule="evenodd"/></svg>dorian@brimcove.com</li>
        <li><svg class="icon" viewBox="0 0 10 10"><path d="M5 0a5 5 0 1 0 0 10A5 5 0 0 0 5 0zm0 1c.7.8 1.1 2.2 1.2 3.5H3.8C3.9 3.2 4.3 1.8 5 1zM1 5.5h1.8c.1 1.3.4 2.4.9 3.2A4 4 0 0 1 1 5.5zm2.8 0h2.4C6.1 6.8 5.7 8.2 5 9c-.7-.8-1.1-2.2-1.2-3.5zm3.4 0H9a4 4 0 0 1-2.7 3.2c.5-.8.8-1.9.9-3.2zM1 4.5a4 4 0 0 1 2.7-3.2c-.5.8-.8 1.9-.9 3.2zm6.2 0c-.1-1.3-.4-2.4-.9-3.2A4 4 0 0 1 9 4.5z"/></svg>www.brimcove.com</li>
      </ul>
    </div>
  </section>
</body>
</html>
```